myQuikTrade Webdesign - trading your electronics for cash - helping you clear up clutter

We need web design (and an updated logo) for a new company based in London called "myQuikTrade". It is a platform that enables users to sell their old electronics for cash, either for themselves or they can donate the cash to charity. In time, we also plan to enable buying of electronics on the site. We specialise in mobile phones, tablets, laptops, and games consoles. Please review pirrowen.com, which is a US site with the same business, and also tunderbrook.co.uk, so have a similar business in the UK. We would like to see designs that use the colour red, and that are bold. We currently have a logo, and a WIP site built, but the design needs to be dramatically improved, the right colour mix needs to be chosen to give a clean and modern feel. Please review www.myquiktrade.com to get an understanding of the work that needs to be improved.

Target Market(s)

People who buy electronics frequently, i.e. upgrade every time a new quince product comes out! These guys usually have a lap top, desk top, tablet and phone.

Industry/Entity Type

Electronics

Logo Text

myQuikTrade

Number of Pages Required

3 page

Font styles to use
Sans Serif

Colors
ec1f27

Requirements
Must have
• Home page design
• "How-it-works" page design
• Sell page design
• Must use the colour red, and have a secondary/accent colour.

```html
<!DOCTYPE html>
<html lang="en">
<head>
<meta charset="utf-8">
<title>myQuikTrade – Sell your electronics for cash</title>
<link href="https://fonts.googleapis.com/css2?family=Roboto:wght@400;500;700&family=Open+Sans:wght@400;600&display=swap" rel="stylesheet">
<style>
:root{
  --red:#ec1f27;
  --navy:#3b3a56;
  --ink:#333338;
  --muted:#8a8a90;
  --light:#f2f2f2;
  --white:#ffffff;
  --green:#8dc63f;
  --yellow:#e6c03a;
  --blue:#45aedb;
  --coral:#f0575a;
  --orange:#f57b2c;
}
*{margin:0;padding:0;box-sizing:border-box}
html,body{width:1200px;height:2683px;overflow:hidden;background:var(--white)}
body{position:relative;font-family:"Open Sans",Arial,sans-serif;color:var(--ink)}
.abs{position:absolute}

/* header */
.site-header{position:absolute;left:0;top:0;width:1200px;height:111px;background:var(--white);z-index:3}
.brand{position:absolute;display:flex;align-items:center;gap:10px}
.brand-mark{width:22px;height:22px;background:var(--red)}
.brand-name{font-family:"Roboto",Arial,sans-serif;font-weight:500;color:var(--red);font-size:25px}
.nav-link{position:absolute;top:46px;font-family:"Roboto",Arial,sans-serif;font-size:11.5px;color:#555;display:flex;align-items:center;gap:7px;letter-spacing:.3px}
.nav-btn{position:absolute;top:36px;width:108px;height:40px;color:var(--white);font-family:"Roboto",Arial,sans-serif;font-size:14px;display:flex;align-items:center;justify-content:center}
.btn-dark{background:var(--navy)}
.btn-red{background:var(--red)}

/* hero */
.hero{position:absolute;left:0;top:111px;width:1200px;height:587px;clip-path:polygon(0 0,1200px 0,1200px 532px,617px 587px,0 533px)}
.hero-left{position:absolute;left:0;top:0;width:617px;height:587px;background:linear-gradient(135deg,#ef3a40,#e31c25 60%,#d81a22)}
.hero-right{position:absolute;left:617px;top:0;width:583px;height:587px;background:linear-gradient(160deg,#c9b8a4,#8a7560 45%,#5b6f86 75%,#a98c72)}
.hero-visual{position:absolute;left:143px;top:121px;width:331px;height:170px;background:#e5363c;border-radius:4px}
.hero-text{position:absolute;left:60px;top:325px;width:496px;text-align:center;color:var(--white);font-size:15px;line-height:21px}
.hero-btn{position:absolute;top:395px;width:158px;height:50px;background:var(--navy);color:var(--white);font-family:"Roboto",Arial,sans-serif;font-size:18px;display:flex;align-items:center;justify-content:center}
.hero-or{position:absolute;left:296px;top:411px;font-size:12px;color:var(--white);font-family:"Roboto",Arial,sans-serif}

/* section titles */
.section-title{position:absolute;left:0;width:1200px;text-align:center;font-family:"Roboto",Arial,sans-serif;font-weight:500;font-size:26px;color:var(--ink)}
.section-lead{position:absolute;left:225px;width:750px;text-align:center;font-size:12.5px;line-height:23px;color:var(--muted)}

/* gadgets */
.gadget{position:absolute;top:888px;width:180px;text-align:center}
.gadget-circle{width:138px;height:138px;margin:0 auto;border-radius:50%;border:5px solid #f1f1f1;box-shadow:0 1px 5px rgba(0,0,0,.12);display:flex;align-items:center;justify-content:center}
.gadget-label{margin-top:26px;font-family:"Roboto",Arial,sans-serif;font-size:13px;color:#444;letter-spacing:.6px}
.carousel-arrow{position:absolute;top:940px}

/* app */
.app-band{position:absolute;left:0;top:1127px;width:1200px;height:492px;background:linear-gradient(100deg,#4a4a66 0%,#3b3a56 45%,#454a63 100%)}
.app-title{position:absolute;left:166px;top:1262px;font-family:"Roboto",Arial,sans-serif;font-weight:700;font-size:38px;color:var(--white)}
.app-title .accent{color:var(--red)}
.app-copy{position:absolute;left:166px;top:1321px;width:510px;font-size:12px;line-height:21.5px;color:var(--white)}
.store-badge{position:absolute;top:1438px;width:158px;height:47px;border-radius:6px;background:#111;border:1px solid #888}
.app-visual{position:absolute;left:660px;top:1127px;width:420px;height:492px;background:linear-gradient(180deg,#55566e,#6c6672 60%,#4a4a60)}
.app-screen{position:absolute;left:842px;top:1202px;width:142px;height:260px;background:var(--white);overflow:hidden}
.screen-brand{position:absolute;left:0;top:78px;width:100%;text-align:center;font-family:"Roboto",Arial,sans-serif;font-weight:500;font-size:17px;color:var(--navy)}
.screen-download{position:absolute;left:0;bottom:0;width:100%;height:104px;background:var(--red);color:var(--white);font-family:"Roboto",Arial,sans-serif;font-size:14px;text-align:center}

/* how to */
.cta-btn{position:absolute;left:467px;top:1810px;width:261px;height:46px;background:var(--red);color:var(--white);font-family:"Roboto",Arial,sans-serif;font-weight:700;font-size:14px;display:flex;align-items:center;justify-content:center}

/* why */
.why{position:absolute;left:0;top:1910px;width:1200px;height:376px;background:var(--light)}
.feature{position:absolute;top:2030px;width:360px;text-align:center}
.feature-icon{height:74px;display:flex;align-items:center;justify-content:center}
.feature-title{margin-top:30px;font-family:"Roboto",Arial,sans-serif;font-weight:500;font-size:15px;color:#222}
.feature-text{margin-top:14px;padding:0 28px;font-size:12px;line-height:24.5px;color:#777}

/* newsletter */
.newsletter{position:absolute;left:0;top:2286px;width:1200px;height:93px;background:var(--red)}
.nl-label{position:absolute;left:145px;top:20px;color:var(--white);font-family:"Roboto",Arial,sans-serif;font-size:13px;line-height:25px}
.nl-label strong{font-size:21px;font-weight:700}
.nl-input{position:absolute;left:336px;top:25px;width:644px;height:39px;background:var(--white);font-size:11px;color:#999;padding:13px 26px;letter-spacing:.3px}
.nl-btn{position:absolute;left:1000px;top:25px;width:120px;height:40px;border:2px solid var(--white);color:var(--white);font-family:"Roboto",Arial,sans-serif;font-weight:700;font-size:13px;display:flex;align-items:center;justify-content:center}

/* footer */
.footer{position:absolute;left:0;top:2379px;width:1200px;height:304px;background:var(--navy);color:var(--white)}
.footer-about{position:absolute;left:80px;top:128px;width:250px;font-size:12px;line-height:23px}
.footer-col{position:absolute;top:42px}
.footer-col h4{font-family:"Roboto",Arial,sans-serif;font-weight:500;font-size:13.5px;color:var(--red);margin-bottom:14px}
.footer-col li{list-style:none;font-size:12px;line-height:22.8px}
.contact-row{display:flex;gap:18px;font-size:12px;line-height:21px;margin-bottom:17px}
.copyright{position:absolute;left:80px;top:265px;font-size:11.5px}
.copyright .accent{color:var(--red)}
.follow{position:absolute;left:848px;top:258px;display:flex;align-items:center;gap:7px;font-size:12px}
.social{width:22px;height:22px;background:var(--red);border-radius:3px}
</style>
</head>
<body>

<header class="site-header">
  <div class="brand" style="left:80px;top:38px">
    <span class="brand-mark"></span><span class="brand-name">myQuikTrade</span>
  </div>
  <div class="nav-link" style="left:545px">
    <svg width="16" height="16" viewBox="0 0 16 16"><circle cx="8" cy="8" r="8" fill="#ec1f27"/><text x="8" y="12" text-anchor="middle" font-size="11" font-weight="700" fill="#fff" font-family="Arial">?</text></svg>
    HOW IT WORKS ?
  </div>
  <div class="nav-btn btn-dark" style="left:706px">BUY</div>
  <div class="nav-btn btn-red" style="left:823px">SELL</div>
  <div class="nav-link" style="left:966px">
    <svg width="12" height="15" viewBox="0 0 12 15"><path d="M0 0h8l4 4v11H0z" fill="#ec1f27"/><path d="M3 8h6M3 11h6" stroke="#fff" stroke-width="1.3"/></svg>
    REGISTER
  </div>
  <div class="nav-link" style="left:1064px">
    <svg width="12" height="14" viewBox="0 0 12 14"><path d="M3 6V4a3 3 0 0 1 6 0v2" fill="none" stroke="#ec1f27" stroke-width="1.8"/><rect x="0" y="6" width="12" height="8" rx="1" fill="#ec1f27"/></svg>
    LOGIN
  </div>
</header>

<section class="hero">
  <div class="hero-left" role="img" aria-label="Red-tinted photo of friends using their phones and gadgets"></div>
  <div class="hero-right" role="img" aria-label="Photo of two young friends outdoors looking at their smartphones"></div>
  <div class="hero-visual" role="img" aria-label="White line illustration of a desktop, tablet, phone and laptop"></div>
  <p class="hero-text">It is a platform that enables users to sell their old electronics for cash, either for themselves or they can donate the cash to charity.</p>
  <div class="hero-btn" style="left:116px">BUY</div>
  <span class="hero-or">OR</span>
  <div class="hero-btn" style="left:343px">SELL</div>
</section>

<h2 class="section-title" style="top:760px">CLICK YOUR GADGET TO SELL</h2>
<p class="section-lead" style="top:809px">Sed ut perspiciatis unde omnis iste natus error sit voluptatem accusantium doloremque laudantium, totam rem aperiam, eaque ipsa quae ab illo inventore veritatis et quasi architecto beatae vitae dicta sunt explicabo.</p>

<svg class="carousel-arrow" style="left:80px" width="16" height="32" viewBox="0 0 16 32"><path d="M14 2L2 16l12 14" fill="none" stroke="#bbb" stroke-width="2.5"/></svg>
<svg class="carousel-arrow" style="left:1101px" width="16" height="32" viewBox="0 0 16 32"><path d="M2 2l12 14L2 30" fill="none" stroke="#bbb" stroke-width="2.5"/></svg>

<div class="gadget" style="left:137px">
  <div class="gadget-circle" style="background:var(--green)">
    <svg width="50" height="44" viewBox="0 0 50 44"><rect x="2" y="2" width="46" height="30" rx="2" fill="none" stroke="#fff" stroke-width="4"/><path d="M20 32v7M13 41h24" stroke="#fff" stroke-width="4"/></svg>
  </div>
  <div class="gadget-label">DESKTOPS</div>
</div>
<div class="gadget" style="left:323px">
  <div class="gadget-circle" style="background:var(--yellow)">
    <svg width="54" height="36" viewBox="0 0 54 36"><rect x="8" y="2" width="38" height="26" rx="2" fill="none" stroke="#fff" stroke-width="4"/><path d="M2 33h50" stroke="#fff" stroke-width="4"/></svg>
  </div>
  <div class="gadget-label">LAPTOPS</div>
</div>
<div class="gadget" style="left:509px">
  <div class="gadget-circle" style="background:var(--blue)">
    <svg width="34" height="46" viewBox="0 0 34 46"><rect x="2" y="2" width="30" height="42" rx="4" fill="none" stroke="#fff" stroke-width="4"/><circle cx="17" cy="37" r="2" fill="#fff"/></svg>
  </div>
  <div class="gadget-label">TABLETS</div>
</div>
<div class="gadget" style="left:695px">
  <div class="gadget-circle" style="background:var(--coral)">
    <svg width="24" height="46" viewBox="0 0 24 46"><rect x="2" y="2" width="20" height="42" rx="4" fill="none" stroke="#fff" stroke-width="4"/><circle cx="12" cy="37" r="2" fill="#fff"/></svg>
  </div>
  <div class="gadget-label">PHONES</div>
</div>
<div class="gadget" style="left:881px">
  <div class="gadget-circle" style="background:var(--orange)">
    <svg width="62" height="34" viewBox="0 0 62 34"><path d="M14 2h34a12 12 0 0 1 12 12v6a12 12 0 0 1-12 12H14A12 12 0 0 1 2 20v-6A12 12 0 0 1 14 2z" fill="#fff"/><path d="M17 10v14M10 17h14" stroke="#f57b2c" stroke-width="4"/><circle cx="43" cy="13" r="3" fill="#f57b2c"/><circle cx="49" cy="20" r="3" fill="#f57b2c"/></svg>
  </div>
  <div class="gadget-label">GAMEING</div>
</div>

<section class="app-band" role="img" aria-label="Darkened photo of a person using a smartphone in the street"></section>
<div class="app-visual" role="img" aria-label="Photo of a hand holding a white smartphone showing the app"></div>
<div class="app-screen">
  <div class="brand-mark" style="position:absolute;left:62px;top:48px;width:18px;height:18px"></div>
  <div class="screen-brand">myQuikTrade</div>
  <div class="screen-download">
    <svg style="margin-top:14px" width="42" height="42" viewBox="0 0 42 42"><circle cx="21" cy="21" r="20" fill="#fff"/><path d="M21 10v16M14 20l7 7 7-7M13 31h16" fill="none" stroke="#ec1f27" stroke-width="3.5"/></svg>
    <div style="margin-top:8px">DOWNLOAD</div>
  </div>
</div>
<h2 class="app-title"><span class="accent">MYQUIKTRADE</span> MOBILE APP</h2>
<p class="app-copy">Lorem ipsum dolor sit amet, consectetur adipiscing elit, sed do eiusmod tempor incididunt ut labore et dolore magna aliqua. Ut enim ad minim veniam, quis nostrud exercitation ullamco laboris nisi ut aliquip ex ea commodo consequat. Duis aute irure dolor in reprehenderit in voluptate velit esse cillum dolore.</p>
<div class="store-badge" style="left:166px"></div>
<div class="store-badge" style="left:336px"></div>

<h2 class="section-title" style="top:1680px">HOW TO SELL YOUR PRODUCT</h2>
<p class="section-lead" style="top:1732px">Sed ut perspiciatis unde omnis iste natus error sit voluptatem accusantium doloremque laudantium, totam rem aperiam, eaque ipsa quae ab illo inventore veritatis et quasi architecto beatae vitae dicta sunt explicabo.</p>
<div class="cta-btn">CLICK HERE TO READ MORE</div>

<section class="why"></section>
<h2 class="section-title" style="top:1955px">WHY CUSTOMERS CHOOSE US</h2>

<div class="feature" style="left:49px">
  <div class="feature-icon">
    <svg width="88" height="70" viewBox="0 0 88 70"><rect x="4" y="22" width="50" height="32" fill="#ec1f27"/><path d="M56 32h16l12 14v8H56z" fill="#ec1f27"/><path d="M62 36h9l8 9H62z" fill="#fff"/><circle cx="20" cy="58" r="8" fill="#ec1f27" stroke="#f2f2f2" stroke-width="3"/><circle cx="70" cy="58" r="8" fill="#ec1f27" stroke="#f2f2f2" stroke-width="3"/><circle cx="20" cy="18" r="14" fill="#f2f2f2" stroke="#ec1f27" stroke-width="4"/><path d="M20 10v9h7" fill="none" stroke="#ec1f27" stroke-width="3"/></svg>
  </div>
  <div class="feature-title">FAST DELIVERY</div>
  <p class="feature-text">Our standard delivery service is FREE in UK, regardless of the size and value. We are committed to offering fast and free delivery.</p>
</div>
<div class="feature" style="left:412px">
  <div class="feature-icon">
    <svg width="96" height="74" viewBox="0 0 96 74"><rect x="10" y="6" width="58" height="38" rx="5" fill="#ec1f27" transform="rotate(-14 39 25)"/><rect x="14" y="20" width="60" height="40" rx="5" fill="#ec1f27" stroke="#f2f2f2" stroke-width="3"/><path d="M14 30h60" stroke="#f2f2f2" stroke-width="5"/><rect x="22" y="40" width="16" height="10" rx="2" fill="#f2f2f2"/><path d="M70 48v-6a8 8 0 0 1 16 0v6" fill="none" stroke="#ec1f27" stroke-width="4"/><rect x="64" y="48" width="28" height="22" rx="3" fill="#ec1f27"/><circle cx="78" cy="58" r="3" fill="#fff"/></svg>
  </div>
  <div class="feature-title">SAFE &amp; SECURE PAYMENT</div>
  <p class="feature-text">Here at myQuikTrade we like to ensure that our customers can purchase from us with confidence &amp; 100% safe and secure payment methods.</p>
</div>
<div class="feature" style="left:788px">
  <div class="feature-icon">
    <svg width="80" height="56" viewBox="0 0 80 56"><rect x="2" y="4" width="76" height="48" rx="2" fill="#ec1f27"/><rect x="10" y="11" width="60" height="34" fill="none" stroke="#fff" stroke-width="2.5"/><circle cx="40" cy="28" r="12" fill="#fff"/><text x="40" y="34" text-anchor="middle" font-size="16" font-weight="700" fill="#ec1f27" font-family="Arial">1</text></svg>
  </div>
  <div class="feature-title">100% MONEY BACK GUARANTED</div>
  <p class="feature-text">To prove our confidence in the services we provide, we are offering a generous 60 day, money back, satisfaction guarantee!</p>
</div>

<section class="newsletter">
  <svg class="abs" style="left:74px;top:26px" width="50" height="40" viewBox="0 0 50 40"><g transform="rotate(-12 25 20)"><rect x="3" y="6" width="44" height="28" rx="2" fill="#fff"/><path d="M3 8l22 15L47 8" fill="none" stroke="#ec1f27" stroke-width="3"/></g></svg>
  <div class="nl-label">NEWSLETTER<br><strong>SUBSCRIPTION</strong></div>
  <div class="nl-input">ENTER EMAIL ADDRESS</div>
  <div class="nl-btn">SUBSCRIBE</div>
</section>

<footer class="footer">
  <div class="brand" style="left:80px;top:78px">
    <span class="brand-mark"></span><span class="brand-name">myQuikTrade</span>
  </div>
  <p class="footer-about">At vero eos et accusamus et iusto odio dignissimos ducimus qui blan</p>

  <div class="footer-col" style="left:365px">
    <h4>QUICK LINKS</h4>
    <ul><li>Contact</li><li>FAQ</li><li>Delivery</li><li>Returns</li><li>Track Orders</li><li>Subscribe</li></ul>
  </div>
  <div class="footer-col" style="left:558px">
    <h4>EXTRAS</h4>
    <ul><li>Specials</li><li>New products</li><li>Top sellers</li><li>Our stores</li><li>Contact us</li><li>About us</li></ul>
  </div>
  <div class="footer-col" style="left:726px">
    <h4>MY ACCOUNT</h4>
    <ul><li>Delivery Information</li><li>Privacy Policy</li><li>Returns Policy</li><li>Terms and Conditions</li><li>FAQs</li></ul>
  </div>
  <div class="footer-col" style="left:950px">
    <h4>CONTACT US</h4>
    <div class="contact-row">
      <svg width="10" height="14" viewBox="0 0 10 14" style="margin-top:3px"><path d="M5 0a5 5 0 0 1 5 5c0 4-5 9-5 9S0 9 0 5a5 5 0 0 1 5-5z" fill="#ec1f27"/><circle cx="5" cy="5" r="2" fill="#3b3a56"/></svg>
      <span>214 Marlow Quay,<br>Harbourside, CA 90412</span>
    </div>
    <div class="contact-row" style="margin-top:12px">
      <svg width="10" height="12" viewBox="0 0 10 12" style="margin-top:4px"><path d="M2 0h3l1 3-2 1.5a7 7 0 0 0 2.5 3L8 5.5l2 1v3L8 12C4 11 0 7 0 2z" fill="#ec1f27"/></svg>
      <span>1 800 555 0142</span>
    </div>
    <div class="contact-row" style="margin-top:20px">
      <svg width="11" height="9" viewBox="0 0 11 9" style="margin-top:6px"><rect width="11" height="9" fill="#ec1f27"/><path d="M0 1l5.5 4L11 1" fill="none" stroke="#3b3a56" stroke-width="1.2"/></svg>
      <span>info@myquiktrade.com</span>
    </div>
  </div>

  <p class="copyright">Copyrights © 2016, <span class="accent">myQuikTrade</span>.  All Rights Reserved</p>
  <div class="follow">
    <span style="margin-right:8px">Follow us on :</span>
    <span class="social"></span><span class="social"></span><span class="social"></span><span class="social"></span><span class="social"></span><span class="social"></span>
  </div>
</footer>

</body>
</html>
```